Küchenparty
Zielgruppe
Restaurant / Catering / Event Management
Zielgruppe ü 40
Aufgabenstellung
Klares, schlichtes und vorallem edles design
Den Valentinstag mal anders feiern?
mischen Sie sich mit Ihren Liebsten ins getrubel einer Großküche und erleben das exclusive Küchenflair!
Bunte Diskobeläuchtung, Musik und Gäste in der Küche....das gibt es nur zu ganz besonderen Anlässen!
Endlich haben Sie in unserer komplett neu renovierten Küche wieder die Möglichkeit unseren Köchen und Köchinnen über die Schulter zu schauen oder über Rezepte fachzusimpeln.
Wir freuen uns Sie zur ersten Küchenparty im Lindmarks am See begrüßen zu dürfen!
Es erwartet Sie eine Veilzahl an speziell für Sie angerichteten Speisen.
Dazu genießen Sie Weine regionaler Weingüter und aus Italien.
Speisen und Getränke inclusive!
Preis pro Person 98€
Den Valentinstag mal anders beginnen;
mit höchstem Genuss aus Küche und Keller bei der Küchenparty im Lindmks am See.
Schlagsworte:
Für Sie individuell angerichtete Speisen / die Küche in action für Sie!
Weine der Region
DJ und Party
Preis 98,00 €
inklusive:
Aperitif
Große Speisenvarietät (5 Gänge plus)
Regionale und italienische Weine
Logo muss vorhanden sein in rot odeer weiss
Kontaktdaten:
Lindmarks am See
Lore-Falk platz 7
71058 Böblingen
Tel: 07031 38 716 0
Mail: event@lindmarks.de
www.lindmarks.de

```html
<!DOCTYPE html>
<html lang="de">
<head>
<meta charset="utf-8">
<title>Küchenparty – Valentinstag</title>
<link href="https://fonts.googleapis.com/css2?family=Questrial&family=PT+Sans:wght@400&display=swap" rel="stylesheet">
<style>
  :root{
    --ink:#0a0a0a;
    --paper:#ffffff;
    --page:#ffffff;
    --brand-red:#9b2a2e;
    --lamp-a:#b59e7a;
    --lamp-b:#8f7a58;
    --dessert-a:#5a3420;
    --dessert-b:#c9c2bb;
    --risotto-a:#efdc9c;
    --risotto-b:#c9a45a;
    --cake-a:#f1e4b4;
    --cake-b:#c23a4f;
    --room-a:#3a2a14;
    --room-b:#caa865;
  }
  *{margin:0;padding:0;box-sizing:border-box}
  html,body{width:1200px;height:1200px;overflow:hidden;background:var(--page)}
  body{position:relative;font-family:"PT Sans",sans-serif;color:var(--ink)}

  .card{position:absolute;width:494px;height:494px;background:var(--paper);
        box-shadow:0 1px 3px rgba(0,0,0,.25);overflow:hidden}
  .card--front{left:77px;top:77px}
  .card--back{left:637px;top:637px}

  /* front grid */
  .cell{position:absolute;width:164.7px;height:164.7px}
  .c0{left:0}.c1{left:164.7px}.c2{left:329.3px}
  .r0{top:0}.r1{top:164.7px}.r2{top:329.3px}
  .photo-lamp{background:radial-gradient(circle at 65% 60%,#ddd0b4 0,var(--lamp-a) 45%,var(--lamp-b) 100%)}
  .photo-dessert{background:linear-gradient(180deg,#8a4a22 0%,var(--dessert-a) 45%,var(--dessert-b) 100%)}
  .photo-risotto{background:radial-gradient(circle at 45% 55%,var(--risotto-a) 0,#e7cd7e 55%,var(--risotto-b) 100%)}
  .photo-cake{background:linear-gradient(160deg,#f6f1ea 0%,var(--cake-a) 45%,var(--cake-b) 100%)}
  .photo-room{background:linear-gradient(180deg,var(--room-a) 0%,#6b4e22 45%,var(--room-b) 100%)}
  .cell--black{background:var(--ink)}
  .hearts{position:absolute;left:50%;top:50%;width:38px;height:24px;transform:translate(-50%,-50%)}

  .front-frame{position:absolute;left:131px;top:131px;width:232px;height:232px;border:2.5px solid var(--ink)}
  .front-title{position:absolute;left:164.7px;top:164.7px;width:164.7px;height:164.7px;text-align:center;font-family:"Questrial",sans-serif}
  .front-title .t1{position:absolute;left:0;right:0;top:26px;font-size:38px;line-height:1;letter-spacing:-1px}
  .front-title .t2{position:absolute;left:0;right:0;top:64px;font-size:48px;line-height:1;letter-spacing:-1px}
  .front-title .rule{position:absolute;left:50%;top:128px;width:61px;height:1.5px;margin-left:-30.5px;background:var(--ink)}
  .front-title .sub{position:absolute;left:0;right:0;top:140px;font-family:"PT Sans",sans-serif;font-size:11px;letter-spacing:1.2px}

  .brand{font-family:"Questrial",sans-serif;white-space:nowrap}
  .brand--white{position:absolute;left:0;right:0;top:72px;text-align:center;color:var(--paper);font-size:17px}

  /* back */
  .photo-lamp-tall{position:absolute;left:0;top:0;width:164px;height:494px;
     background:radial-gradient(ellipse at 80% 70%,#e4d6b8 0,var(--lamp-a) 45%,var(--lamp-b) 100%)}
  .back-box{position:absolute;left:184px;top:30px;width:280px;height:107px;border:3px solid var(--ink);text-align:center}
  .back-box .h{font-family:"Questrial",sans-serif;font-size:17.5px;line-height:24px;margin-top:8px;letter-spacing:-.2px}
  .back-box .rule{width:60px;height:1.5px;background:var(--ink);margin:9px auto 0}
  .back-box .sub{font-size:10.5px;letter-spacing:1.6px;margin-top:9px}
  .back-copy{position:absolute;left:164px;right:0;text-align:center;font-size:8.6px;line-height:11px}
  .back-rule{position:absolute;left:545px;width:35px;height:1.5px;background:var(--ink)}
  .back-rule{left:auto}
  .rule-line{position:absolute;left:305px;width:35px;height:1.5px;background:var(--ink)}
  .contact{position:absolute;top:438px;font-size:6.6px;line-height:9px}
  .contact--address{left:182px}
  .contact--reach{left:272px}
  .brand--red{position:absolute;left:378px;top:444px;color:var(--brand-red);font-size:13px}
</style>
</head>
<body>

<section class="card card--front">
  <div class="cell c0 r0 photo-lamp" role="img" aria-label="Foto: Kugelleuchte aus Drahtgeflecht"></div>
  <div class="cell c1 r0 photo-dessert" role="img" aria-label="Foto: Schokoladendessert mit Blüte"></div>
  <div class="cell c2 r0"><svg class="hearts" viewBox="0 0 38 24"><path d="M12 24 L1.5 12 A6 6 0 0 1 12 4.5 A6 6 0 0 1 22.5 12 Z" fill="#0a0a0a"/><path d="M26 24 L15.5 12 A6 6 0 0 1 26 4.5 A6 6 0 0 1 36.5 12 Z" fill="#0a0a0a" stroke="#fff" stroke-width="1"/></svg></div>

  <div class="cell c0 r1 photo-risotto" role="img" aria-label="Foto: Risotto mit Tomate und Rosmarin"></div>
  <div class="cell c2 r1 photo-cake" role="img" aria-label="Foto: Törtchen mit Walnüssen und Beerensauce"></div>

  <div class="cell c0 r2 photo-room" role="img" aria-label="Foto: gedeckte Tafel im Restaurant"></div>
  <div class="cell c1 r2"><svg class="hearts" viewBox="0 0 38 24"><path d="M12 24 L1.5 12 A6 6 0 0 1 12 4.5 A6 6 0 0 1 22.5 12 Z" fill="#0a0a0a"/><path d="M26 24 L15.5 12 A6 6 0 0 1 26 4.5 A6 6 0 0 1 36.5 12 Z" fill="#0a0a0a" stroke="#fff" stroke-width="1"/></svg></div>
  <div class="cell c2 r2 cell--black"><div class="brand brand--white">Lindmarks am See</div></div>

  <div class="front-frame"></div>
  <div class="front-title">
    <div class="t1">KÜCHEN</div>
    <div class="t2">PARTY</div>
    <div class="rule"></div>
    <div class="sub">Valentinstag</div>
  </div>
</section>

<section class="card card--back">
  <div class="photo-lamp-tall" role="img" aria-label="Foto: leuchtende Kugelleuchten aus Drahtgeflecht"></div>

  <div class="back-box">
    <div class="h">DEN VALENTINSTAG<br>MAL ANDERS FEIERN?</div>
    <div class="rule"></div>
    <div class="sub">VALENTINSTAG</div>
  </div>

  <p class="back-copy" style="top:173px">mit höchstem Genuss aus Küche und Keller bei der Küchenparty<br>im Lindmks am See.</p>
  <div class="rule-line" style="top:205px"></div>
  <p class="back-copy" style="top:228px">Für Sie individuell angerichtete Speisen / die Küche in action für Sie!<br>Weine der Region<br>DJ und Party</p>
  <div class="rule-line" style="top:275px"></div>
  <p class="back-copy" style="top:295px">Preis 98,00 €&nbsp; inklusive: Aperitif Große Speisenvarietät<br>(5 Gänge plus) Regionale und italienische Weine</p>

  <p class="contact contact--address">Lindmarks am See<br>Lore-Falk platz 7<br>71058 Böblingen</p>
  <p class="contact contact--reach">Tel: 07031 38 716 0<br>Mail: event@lindmarks.de<br>www.lindmarks.de</p>
  <div class="brand brand--red">Lindmarks am See</div>
</section>

</body>
</html>
```